Online campaigning platform needs web design

We need designs for our start a survey page and company overview page (undesigned elements attached). Our platform allows people to crowd-source better workplace policies and push them to become a reality.
The company name is Veltrane Hub and the primary colour is teal, with secondary colours of white, dark grey and green. The company logo is attached.
Website needs to be modern, clean and simple. As part of the design I would like to see iconography representing concepts like: secure, safety in numbers, teamwork, registration, insights (or results) and email.
We will provide feedback regardless of the quality of the design to ensure a better outcome for all parties.
Please feel free to contact us if you have any questions.
# The designer can use placeholder images or feel free to use any/all or none of the attached images
# The designer can use sample filler text
Under 40s
It Company
2 page

```html
<!DOCTYPE html>
<html lang="en">
<head>
<meta charset="utf-8">
<title>Veltrane Hub – Take Part. Lead</title>
<link href="https://fonts.googleapis.com/css2?family=Varela+Round&display=swap" rel="stylesheet">
<style>
  :root {
    --teal: #0aa4c3;
    --teal-deep: #1aa39a;
    --teal-text: #13a3c4;
    --dark-grey: #4a4a4a;
    --mid-grey: #666666;
    --white: #ffffff;
    --hero-dark: #2b2e33;
    --hero-mid: #5a5650;
  }
  * { margin: 0; padding: 0; box-sizing: border-box; }
  html, body { width: 800px; height: 1200px; overflow: hidden; background: var(--white); }
  body { font-family: "Varela Round", sans-serif; color: var(--dark-grey); position: relative; }

  .site-header { position: absolute; top: 0; left: 0; width: 800px; height: 44px; background: var(--white); border-bottom: 1px solid #d9d9d9; }
  .brand { position: absolute; left: 32px; top: 11px; display: flex; align-items: center; gap: 8px; }
  .brand-dot { width: 18px; height: 18px; border-radius: 50%; background: var(--teal); }
  .brand-name { font-size: 17px; color: var(--teal); }
  .main-nav { position: absolute; right: 26px; top: 20px; display: flex; gap: 11px; font-size: 11px; color: var(--dark-grey); }

  .hero { position: absolute; top: 44px; left: 0; width: 800px; height: 304px;
    background: radial-gradient(ellipse at 55% 55%, #8a847c 0%, var(--hero-mid) 35%, var(--hero-dark) 80%); }
  .hero-photo { position: absolute; inset: 0; }
  .hero-title { position: absolute; top: 84px; width: 100%; text-align: center; font-size: 32px; color: var(--white); font-weight: 400; }
  .hero-subtitle { position: absolute; top: 128px; width: 100%; text-align: center; font-size: 12px; color: var(--white); }
  .hero-arrow { position: absolute; top: 116px; }
  .hero-arrow.prev { left: 18px; }
  .hero-arrow.next { right: 18px; }
  .hero-band { position: absolute; top: 348px; left: 0; width: 800px; height: 11px; background: var(--teal-deep); }

  .about { position: absolute; top: 359px; left: 0; width: 800px; height: 219px; }
  .about-heading { position: absolute; right: 544px; top: 55px; text-align: right; font-size: 22px; line-height: 27px; color: var(--teal-text); font-weight: 400; }
  .about-body { position: absolute; left: 302px; top: 30px; width: 441px; font-size: 9.2px; line-height: 11.6px; color: var(--mid-grey); text-align: justify; }
  .about-body p + p { margin-top: 11.6px; }

  .why { position: absolute; top: 578px; left: 0; width: 800px; height: 408px; background: var(--teal); color: var(--white); }
  .why-title { position: absolute; top: 12px; width: 100%; text-align: center; font-size: 22px; font-weight: 400; }
  .feature { position: absolute; width: 160px; text-align: center; }
  .feature-icon { display: block; margin: 0 auto; }
  .feature-name { font-size: 12px; font-weight: 400; margin-top: 14px; }
  .feature-text { font-size: 6.6px; line-height: 9.6px; text-align: justify; margin-top: 10px; }

  .survey { position: absolute; top: 986px; left: 0; width: 800px; height: 214px; }
  .survey-title { position: absolute; top: 28px; width: 100%; text-align: center; font-size: 22px; font-weight: 400; color: var(--dark-grey); }
  .survey-text { position: absolute; left: 70px; top: 66px; width: 677px; font-size: 9.4px; line-height: 12px; color: var(--mid-grey); text-align: justify; text-align-last: justify; }
  .start-button { position: absolute; left: 311px; top: 121px; width: 151px; height: 51px; border-radius: 6px; background: var(--teal); color: var(--white); font-family: inherit; font-size: 23px; border: none; }
</style>
</head>
<body>
  <header class="site-header">
    <div class="brand"><span class="brand-dot"></span><span class="brand-name">Veltrane Hub</span></div>
    <nav class="main-nav"><span>HOME</span><span>OVERVIEW</span><span>HISTORY</span><span>JOIN US</span><span>OUR REACH</span></nav>
  </header>

  <section class="hero">
    <div class="hero-photo" role="img" aria-label="Photo of hands typing on a laptop keyboard"></div>
    <h1 class="hero-title">Take Part. Lead</h1>
    <p class="hero-subtitle">Your opinion matters. Take part in our survey to bring change.</p>
    <svg class="hero-arrow prev" width="18" height="22" viewBox="0 0 18 22"><polyline points="16,1 2,11 16,21" fill="none" stroke="#fff" stroke-width="1.6"/></svg>
    <svg class="hero-arrow next" width="18" height="22" viewBox="0 0 18 22"><polyline points="2,1 16,11 2,21" fill="none" stroke="#fff" stroke-width="1.6"/></svg>
  </section>
  <div class="hero-band"></div>

  <section class="about">
    <h2 class="about-heading">About<br>Veltrane<br>Hub</h2>
    <div class="about-body">
      <p>It is a long established fact that a reader will be distracted by the readable content of a page when looking at its layout. The point of using Lorem Ipsum is that it has a more-or-less normal distribution of letters, as opposed to using 'Content here, content here', making it look like readable English. Many desktop publishing packages and web page editors now use Lorem Ipsum as their default model text, and a search for 'lorem ipsum' will uncover many web sites still in their infancy. Various versions have evolved over the years, sometimes by accident, sometimes on purpose (injected humour and the like)</p>
      <p>It is a long established fact that a reader will be distracted by the readable content of a page when looking at its layout. The point of using Lorem Ipsum is that it has a more-or-less normal distribution of letters, as opposed to using 'Content here, content here', making it look like readable English. Many desktop publishing packages and web page editors now use Lorem Ipsum as their default model text, and a search for 'lorem ipsum' will uncover many web sites still in their infancy. Various versions have evolved over the years, sometimes by accident, sometimes on purpose (injected humour and the like)</p>
    </div>
  </section>

  <svg width="0" height="0" style="position:absolute">
    <defs>
      <symbol id="icon-shield" viewBox="0 0 34 34">
        <circle cx="17" cy="17" r="16" fill="none" stroke="#fff" stroke-width="1.2"/>
        <path d="M17 8 L24 11 V17 C24 21 21 24 17 26 C13 24 10 21 10 17 V11 Z" fill="#fff"/>
        <polyline points="13.5,17 16,19.5 20.5,14.5" fill="none" stroke="#0aa4c3" stroke-width="1.6"/>
      </symbol>
      <symbol id="icon-lock" viewBox="0 0 34 34">
        <circle cx="17" cy="17" r="16" fill="none" stroke="#fff" stroke-width="1.2"/>
        <path d="M13.5 16 V13.5 A3.5 3.5 0 0 1 20.5 13.5 V16" fill="none" stroke="#fff" stroke-width="1.6"/>
        <rect x="12" y="16" width="10" height="8" rx="1" fill="#fff"/>
      </symbol>
      <symbol id="icon-team" viewBox="0 0 34 34">
        <circle cx="17" cy="17" r="16" fill="none" stroke="#fff" stroke-width="1.2"/>
        <circle cx="17" cy="11" r="2.2" fill="none" stroke="#fff" stroke-width="1.1"/>
        <path d="M13.5 17 a3.5 3.5 0 0 1 7 0 Z" fill="none" stroke="#fff" stroke-width="1.1"/>
        <circle cx="12" cy="19" r="2.2" fill="none" stroke="#fff" stroke-width="1.1"/>
        <path d="M8.5 25 a3.5 3.5 0 0 1 7 0 Z" fill="none" stroke="#fff" stroke-width="1.1"/>
        <circle cx="22" cy="19" r="2.2" fill="none" stroke="#fff" stroke-width="1.1"/>
        <path d="M18.5 25 a3.5 3.5 0 0 1 7 0 Z" fill="none" stroke="#fff" stroke-width="1.1"/>
      </symbol>
    </defs>
  </svg>

  <section class="why">
    <h2 class="why-title">Why Our Platform?</h2>

    <div class="feature" style="left:84px; top:73px;">
      <svg class="feature-icon" width="34" height="34"><use href="#icon-shield"/></svg>
      <h3 class="feature-name">Secure</h3>
      <p class="feature-text">It is a long established fact that a reader will be distracted by the readable content of a page when looking at its layout. The point of using Lorem Ipsum is that it has a more-or-less normal distribution of letters, as opposed .</p>
    </div>
    <div class="feature" style="left:314px; top:73px;">
      <svg class="feature-icon" width="34" height="34"><use href="#icon-lock"/></svg>
      <h3 class="feature-name">Safety in Numbers</h3>
      <p class="feature-text">It is a long established fact that a reader will be distracted by the readable content of a page when looking at its layout. The point of using Lorem Ipsum is that it has a more-or-less normal distribution of letters, as opposed .</p>
    </div>
    <div class="feature" style="left:530px; top:73px;">
      <svg class="feature-icon" width="34" height="34"><use href="#icon-team"/></svg>
      <h3 class="feature-name">Teamwork</h3>
      <p class="feature-text">It is a long established fact that a reader will be distracted by the readable content of a page when looking at its layout. The point of using Lorem Ipsum is that it has a more-or-less normal distribution of letters, as opposed .</p>
    </div>

    <div class="feature" style="left:98px; top:239px;">
      <svg class="feature-icon" width="34" height="34" style="margin-left:50px"><use href="#icon-shield"/></svg>
      <h3 class="feature-name">Registration</h3>
      <p class="feature-text" style="margin-left:-9px">It is a long established fact that a reader will be distracted by the readable content of a page when looking at its layout. The point of using Lorem Ipsum is that it has a more-or-less normal distribution of letters, as opposed .</p>
    </div>
    <div class="feature" style="left:314px; top:239px;">
      <svg class="feature-icon" width="34" height="34"><use href="#icon-lock"/></svg>
      <h3 class="feature-name">Insights (results)</h3>
      <p class="feature-text">It is a long established fact that a reader will be distracted by the readable content of a page when looking at its layout. The point of using Lorem Ipsum is that it has a more-or-less normal distribution of letters, as opposed .</p>
    </div>
    <div class="feature" style="left:530px; top:239px;">
      <svg class="feature-icon" width="34" height="34"><use href="#icon-team"/></svg>
      <h3 class="feature-name">Email</h3>
      <p class="feature-text">It is a long established fact that a reader will be distracted by the readable content of a page when looking at its layout. The point of using Lorem Ipsum is that it has a more-or-less normal distribution of letters, as opposed .</p>
    </div>
  </section>

  <section class="survey">
    <h2 class="survey-title">Take a Survey</h2>
    <p class="survey-text">It is a long established fact that a reader will be distracted by the readable content of a page when looking at its layout. The point of using Lorem Ipsum is that it has a more-or-less normal distribution of letters, as opposed to using 'Content here, content here', making it look like readable English.</p>
    <button class="start-button">Start</button>
  </section>
</body>
</html>
```